Real Estate "For Sale" Sign for construction company

We need a sign that we can use to hang on a post and place on the road when we sell a property. The sign will be simple and will need to mainly feature our logo (files attached), as well as the words "For Sale", and then our phone number "(555) 617 3489". The sign will hang on a post that'll look something like the attached picture.

Target Market(s)

Home buyers

Industry/Entity Type

Real Estate

Font styles to use
Serif
Sans Serif

Colors
0054AA
0677BA
7BADD7
CADEEF
E8F1F8
0094D4
00A9DD
6FCCEA
C7EBF8
E9F6FB

Requirements
Must have
• For Sale & our phone number

```html
<!DOCTYPE html>
<html lang="en">
<head>
<meta charset="utf-8">
<title>For Sale Sign – Larkspur Realty</title>
<link rel="stylesheet" href="https://fonts.googleapis.com/css2?family=Montserrat:wght@500;900&display=swap">
<style>
  :root {
    --sky: #8fd6f6;
    --sky-ray: #84c9e6;
    --sky-ring: #c8e9fb;
    --navy: #233a7b;
    --brand-blue: #1a7cc1;
    --brand-dot: #0677ba;
    --white: #ffffff;
  }
  * { margin: 0; padding: 0; box-sizing: border-box; }
  html, body { width: 946px; height: 1200px; overflow: hidden; background: var(--white); }
  body { font-family: "Montserrat", Arial, sans-serif; }

  .sign { position: relative; width: 946px; height: 1200px; overflow: hidden; background: var(--white); }

  .sign__sky { position: absolute; left: 0; top: 0; width: 946px; height: 768px; background: var(--sky); }
  .sign__decor { position: absolute; left: 0; top: 0; }

  .sign__headline {
    position: absolute; left: 0; width: 946px;
    color: var(--navy); font-weight: 900; text-align: center;
    line-height: 1; font-size: 280px;
  }
  .sign__headline--for { top: 50px; letter-spacing: -2px; padding-left: 22px; }
  .sign__headline--sale { top: 310px; letter-spacing: -6px; }

  .sign__brand-band { position: absolute; left: 0; top: 768px; width: 946px; height: 231px; background: var(--white); }

  .brand-name {
    position: absolute; left: 0; top: 848px; width: 946px;
    text-align: center; color: var(--brand-blue);
    font-weight: 500; font-size: 74px; line-height: 1; letter-spacing: -1px;
  }

  .sign__contact-band { position: absolute; left: 0; top: 999px; width: 946px; height: 201px; background: var(--navy); }
  .contact__icon { position: absolute; left: 94px; top: 1051px; }
  .contact__phone {
    position: absolute; left: 190px; top: 1040px;
    color: var(--white); font-weight: 500; font-size: 84px; line-height: 1; letter-spacing: -1px;
  }
</style>
</head>
<body>
<main class="sign">
  <div class="sign__sky"></div>
  <svg class="sign__decor" width="946" height="999" viewBox="0 0 946 999" aria-hidden="true">
    <polygon points="0,0 25,0 260,190 180,250 0,90" fill="var(--sky-ray)" opacity="0.45"/>
    <polygon points="0,150 190,300 130,340 0,230" fill="var(--sky-ray)" opacity="0.35"/>
    <polygon points="946,40 946,250 760,380 700,330" fill="var(--sky-ray)" opacity="0.45"/>
    <polygon points="946,290 946,340 800,450 780,430" fill="var(--sky-ray)" opacity="0.35"/>
    <circle cx="465" cy="870" r="240" fill="var(--sky-ring)"/>
  </svg>

  <h1 class="sign__headline sign__headline--for">FOR</h1>
  <div class="sign__headline sign__headline--sale">SALE</div>

  <section class="sign__brand-band"></section>
  <svg class="sign__decor" width="946" height="999" viewBox="0 0 946 999" aria-hidden="true">
    <circle cx="465" cy="870" r="224" fill="var(--white)"/>
    <circle cx="465" cy="760" r="58" fill="var(--brand-dot)"/>
  </svg>
  <div class="brand-name">Larkspur Realty</div>

  <section class="sign__contact-band"></section>
  <svg class="contact__icon" width="84" height="84" viewBox="0 0 84 84" aria-label="Phone">
    <circle cx="42" cy="42" r="42" fill="var(--sky)"/>
    <path d="M29 22c2-1 4 0 5 2l4 7c1 2 0 4-1 5l-3 2c2 5 6 9 11 11l2-3c1-1 3-2 5-1l7 4c2 1 3 3 2 5l-2 4c-2 3-5 4-9 3-12-4-21-13-25-25-1-4 0-7 3-9z" fill="none" stroke="var(--navy)" stroke-width="4" stroke-linejoin="round"/>
    <path d="M46 28a10 10 0 0 1 10 10M47 20a18 18 0 0 1 17 17" fill="none" stroke="var(--navy)" stroke-width="3.5" stroke-linecap="round"/>
  </svg>
  <div class="contact__phone">(555) 617 3489</div>
</main>
</body>
</html>
```